New template needed for Joomla 3.2 website

We are a mortgage origination company based in Johannesburg, South Africa and require a sleek, modern & professional look for our website.
The website is complete and your template should accommodate all pages on the site (there are not many) and be ready for Joomla implementation.
Our website can be viewed at www.kestrelbondhouse.co.za
Target Market(s)
We are targeting consumers who require mortgage finance to buy real estate. There is no particular demographic, except that we cater to South African home buyers exclusively!
Requirements
Must have
- It must look professional and modern.
Take a look at competitor websites:
www.ziru.co.za
www.velmabonds.com
http://www.tarnvalegroup.co.za/lendcrest/
http://www.quillfund.co.za/
We want to beat the competition !!
Nice to have
- Website should blend with company logo and play on the symbol in the logo.
I want more of a people / photo element to the template. It needs to make us seem "tangible"

```html
<!DOCTYPE html>
<html lang="en">
<head>
<meta charset="utf-8">
<title>Kestrel Bond House</title>
<link href="https://fonts.googleapis.com/css2?family=Lato:wght@400;700&family=Roboto+Condensed:wght@700&display=swap" rel="stylesheet">
<style>
:root{
  --blue:#1a6faf;
  --blue-dark:#0f5a94;
  --ink:#333;
  --muted:#555;
  --line:#dcdcdc;
  --band:#f2f2f2;
  --footer:#2b2b2b;
  --footer-text:#d8d8d8;
}
*{box-sizing:border-box;margin:0;padding:0}
html,body{width:839px;height:1200px;overflow:hidden;background:#fff}
body{font-family:'Lato',sans-serif;color:var(--ink);position:relative}
a{color:var(--blue)}

/* header */
.site-header{position:absolute;left:0;top:0;width:839px;height:64px;background:#fff;z-index:2}
.brand{position:absolute;left:93px;top:14px;display:flex;align-items:center;gap:7px}
.brand-dot{width:30px;height:30px;border-radius:50%;background:var(--blue)}
.brand-name{font-size:20px;font-weight:700;color:var(--blue)}
.main-nav{position:absolute;left:359px;top:0;display:flex;height:64px}
.main-nav a{display:flex;flex-direction:column;align-items:center;justify-content:flex-end;padding-bottom:11px;height:64px;font-size:11px;color:#333;text-decoration:none;border-right:1px solid #e2e2e2}
.main-nav a svg{margin-bottom:6px}
.main-nav a.active{background:var(--blue);color:#fff;font-weight:700;border-right:none}

/* hero */
.hero{position:absolute;left:0;top:64px;width:839px;height:347px;background:linear-gradient(180deg,#8ea5b6 0%,#7d6d5d 30%,#6e7f4a 62%,#5d8a2e 100%)}
.hero-glow{position:absolute;left:454px;top:20px;width:294px;height:276px;border-radius:50%;background:rgba(255,255,255,.22)}
.hero-copy{position:absolute;left:503px;top:100px;color:#fff}
.hero-copy h1{font-family:'Roboto Condensed',sans-serif;font-weight:700;line-height:1.05;color:#fff;text-shadow:0 1px 2px rgba(0,0,0,.4)}
.hero-copy h1 .title-top{display:block;font-size:25px}
.hero-copy h1 .title-main{display:block;font-size:31px;margin-top:6px}
.hero-copy p{font-size:13px;line-height:18px;margin-top:10px;width:210px;text-shadow:0 1px 2px rgba(0,0,0,.4)}
.btn-apply{display:inline-flex;align-items:center;gap:9px;margin-top:21px;height:28px;padding:0 4px 0 13px;border-radius:14px;background:var(--blue);color:#fff;font-size:13px;text-decoration:none;box-shadow:0 2px 3px rgba(0,0,0,.3)}
.btn-apply span.arrow{width:20px;height:20px;border-radius:50%;background:#fff;display:flex;align-items:center;justify-content:center}
.hero-dots{position:absolute;left:694px;top:325px;display:flex;gap:5px}
.hero-dots i{width:10px;height:10px;border-radius:50%;background:rgba(255,255,255,.35)}
.hero-dots i.on{background:var(--blue);border:2px solid #fff}

/* feature cards */
.cards{position:absolute;left:92px;top:430px;display:flex;gap:18px}
.card{width:150px;height:164px;border:1px solid var(--line);border-radius:3px;position:relative;overflow:hidden;background:#fff}
.card h3{display:flex;align-items:center;gap:6px;margin:6px 8px 0;padding-bottom:6px;font-size:13.5px;font-weight:400;color:var(--blue);border-bottom:1px dashed var(--line)}
.mark{width:16px;height:16px;border-radius:50%;background:var(--blue);flex:none}
.card p{font-size:9px;line-height:13.5px;color:var(--muted);margin:8px 9px 0}
.card .more{position:absolute;right:12px;top:80px;font-size:9px;text-decoration:underline}
.card .visual{position:absolute;left:0;bottom:0;width:100%;height:72px}
.v-coins{background:linear-gradient(180deg,#fff 0%,#e8f0d8 45%,#c79a55 100%)}
.v-family{background:linear-gradient(180deg,#fff 0%,#e9c9b4 40%,#b34a3a 100%)}
.v-house{background:linear-gradient(180deg,#fff 0%,#e6e9ee 50%,#9aa7b6 100%)}
.v-calc{background:linear-gradient(180deg,#fff 0%,#d9d9d9 45%,#8a8a8a 100%)}

.divider{position:absolute;left:92px;top:616px;width:655px;height:1px;background:linear-gradient(90deg,transparent,#ddd,transparent)}

/* welcome */
.welcome{position:absolute;left:92px;top:640px;width:364px}
.welcome h2{display:flex;align-items:center;gap:7px;font-size:18px;font-weight:400;color:#222;padding-bottom:9px;border-bottom:1px dashed var(--line)}
.welcome h2 .mark{width:24px;height:24px}
.welcome h2 em{font-style:normal;color:var(--blue)}
.welcome p{font-size:9px;line-height:14.6px;color:var(--muted);margin-top:12px}
.welcome h4{font-size:11px;color:var(--blue);font-weight:700;margin-top:11px}
.welcome h4 + p{margin-top:3px}
.welcome .read{display:block;text-align:right;font-size:9px;margin-top:9px;text-decoration:underline}
.welcome-rule{position:absolute;left:475px;top:644px;width:1px;height:178px;background:#eee}

.perks{position:absolute;left:490px;top:642px}
.perk{position:relative;width:257px;height:54px;margin-bottom:9px;padding-left:60px}
.perk .box{position:absolute;left:14px;top:0;right:0;bottom:0;background:#f1f1f1;border:1px solid #e2e2e2;border-radius:3px}
.perk .icon{position:absolute;left:0;top:0;width:54px;height:54px;border-radius:50%;background:var(--blue);border:3px solid #fff;box-shadow:0 0 0 1px #d6d6d6;display:flex;align-items:center;justify-content:center}
.perk h5{position:relative;font-size:12px;font-weight:400;color:#222;margin-top:6px}
.perk p{position:relative;font-size:8.5px;line-height:11.5px;color:#666;margin-top:4px;width:190px}
.perk .more{position:absolute;right:11px;bottom:5px;font-size:8px;font-weight:700;text-decoration:none}

/* lenders */
.lenders{position:absolute;left:0;top:855px;width:839px;height:143px;background:var(--band)}
.lenders h2{text-align:center;font-size:16.5px;font-weight:400;color:#222;margin-top:15px}
.lenders h2 em{font-style:normal;color:var(--blue)}
.lender-row{position:absolute;left:92px;top:44px;width:655px;height:72px;background:#fff;border:1px solid var(--line);border-radius:4px;display:flex;align-items:center;justify-content:space-around;padding:0 30px}
.lender{display:flex;align-items:center;gap:6px;font-size:16px;font-weight:700}
.lender i{width:16px;height:16px;border-radius:50%}
.lender-a{color:#1f8f86}.lender-a i{background:#f0a020}
.lender-b{color:#145a3a}.lender-b i{background:#145a3a}
.lender-c{color:#d52b1e}.lender-c i{background:#d52b1e}
.lender-d{color:#0b2d7a}.lender-d i{background:#0b2d7a}
.pager{position:absolute;top:70px;width:22px;height:22px;border-radius:50%;background:#f4f4f4;border:1px solid #ccc;display:flex;align-items:center;justify-content:center}

/* footer */
.site-footer{position:absolute;left:0;top:998px;width:839px;height:175px;background:var(--footer);color:var(--footer-text)}
.fcol{position:absolute;top:17px}
.fcol h3{font-size:12px;font-weight:400;color:#fff;padding-bottom:8px;border-bottom:1px dashed #555}
.f-links{left:92px;width:80px}
.f-links ul{list-style:none;margin-top:7px}
.f-links li{font-size:9px;line-height:16.8px;padding-left:12px;position:relative}
.f-links li::before{content:"›";position:absolute;left:2px;color:#aaa}
.f-news{left:223px;width:150px}
.f-news p{font-size:9px;line-height:13.5px;margin-top:9px}
.f-news .field{margin-top:7px;width:149px;height:20px;background:#fff;border-radius:2px;font-size:8px;font-style:italic;color:#666;padding:5px 7px}
.f-news .sub{margin-top:9px;display:inline-block;background:var(--blue);color:#fff;font-size:9px;padding:5px 7px;border-radius:2px}
.f-rule{position:absolute;top:22px;width:1px;height:140px;background:#3c3c3c}
.f-contact{left:429px;width:318px}
.c-row{position:absolute;left:0;display:flex;gap:10px;font-size:9px;line-height:13px;color:#e8e8e8}
.c-row svg{flex:none;margin-top:1px}
.map{position:absolute;left:151px;top:33px;width:167px;height:96px;border:3px solid #fff;background:linear-gradient(135deg,#e4e4e4 0%,#d6d8da 100%)}

.bottom-bar{position:absolute;left:0;top:1173px;width:839px;height:27px;background:var(--blue);color:#fff;font-size:9px}
.bottom-bar .copy{position:absolute;left:94px;top:8px}
.bottom-bar .follow{position:absolute;right:91px;top:6px;display:flex;align-items:center;gap:8px;font-size:10.5px;font-weight:700}
.bottom-bar .follow i{width:10px;height:10px;border-radius:50%;background:#fff}
</style>
</head>
<body>

<header class="site-header">
  <div class="brand"><span class="brand-dot"></span><span class="brand-name">Kestrel Bond House</span></div>
  <nav class="main-nav">
    <a class="active" style="width:59px">
      <svg width="18" height="16" viewBox="0 0 18 16"><path d="M9 1 1 8h2.5v7h4v-4h3v4h4V8H17z" fill="#fff"/></svg>Home</a>
    <a style="width:75px">
      <svg width="16" height="17" viewBox="0 0 16 17"><circle cx="8" cy="5" r="4" fill="var(--blue)"/><path d="M1 17c0-5 3-7 7-7s7 2 7 7z" fill="var(--blue)"/></svg>About Us</a>
    <a style="width:85px">
      <svg width="18" height="17" viewBox="0 0 18 17"><rect x="2" y="1" width="11" height="15" rx="1" fill="none" stroke="var(--blue)" stroke-width="1.8"/><path d="M5 6h5M5 9h5M5 12h3" stroke="var(--blue)" stroke-width="1.4"/><path d="M10 13 16 5" stroke="var(--blue)" stroke-width="2.2"/></svg>Information</a>
    <a style="width:85px">
      <svg width="14" height="17" viewBox="0 0 14 17"><rect x="1" y="1" width="12" height="15" rx="1.5" fill="none" stroke="var(--blue)" stroke-width="1.8"/><rect x="3.5" y="3.5" width="7" height="3" fill="var(--blue)"/><path d="M4 9h1M7 9h1M10 9h0.5M4 12h1M7 12h1M10 12h0.5" stroke="var(--blue)" stroke-width="1.8"/></svg>Calculators</a>
    <a style="width:83px;border-right:none">
      <svg width="20" height="15" viewBox="0 0 20 15"><rect x="1" y="1" width="18" height="13" fill="none" stroke="var(--blue)" stroke-width="1.8"/><path d="M1 1l9 7 9-7" fill="none" stroke="var(--blue)" stroke-width="1.8"/></svg>Contact Us</a>
  </nav>
</header>

<section class="hero" role="img" aria-label="Photo of a smiling family of four sitting on the lawn in front of their stone-clad house">
  <div class="hero-glow"></div>
  <div class="hero-copy">
    <h1><span class="title-top">FAST HOMELOANS</span><span class="title-main">GREAT SERVICE !</span></h1>
    <p>Dream to by a home get the best deal from Kestrel Bond House</p>
    <a class="btn-apply">Apply Online <span class="arrow"><svg width="11" height="10" viewBox="0 0 11 10"><path d="M1 5h8M5.5 1 9.5 5 5.5 9" fill="none" stroke="var(--blue)" stroke-width="2"/></svg></span></a>
  </div>
  <div class="hero-dots"><i class="on"></i><i></i><i></i><i></i></div>
</section>

<section class="cards">
  <article class="card">
    <h3><span class="mark"></span>Referral Program</h3>
    <p>Click on the button below to join our lead referal program and start earning money.</p>
    <a class="more">JOIN TODAY</a>
    <div class="visual v-coins" role="img" aria-label="Seedling growing from a pile of coins"></div>
  </article>
  <article class="card">
    <h3><span class="mark"></span>Get Pre Qualified</h3>
    <p>Our experienced consultants would be happy to prequalify you for a homeloan.</p>
    <a class="more">APPLY NOW</a>
    <div class="visual v-family" role="img" aria-label="Photo of a happy young family"></div>
  </article>
  <article class="card">
    <h3><span class="mark"></span>Ask a Question</h3>
    <p>Ask an experienced consultant to answer all your questions about homeloan finance.</p>
    <a class="more">ASK NOW</a>
    <div class="visual v-house" role="img" aria-label="Model house on paperwork with a question mark"></div>
  </article>
  <article class="card">
    <h3><span class="mark"></span>Calculators</h3>
    <p>Find out what you can afford with our convenient finance calculators.</p>
    <a class="more">CALCULATE</a>
    <div class="visual v-calc" role="img" aria-label="Model house standing on a calculator"></div>
  </article>
</section>

<div class="divider"></div>

<section class="welcome">
  <h2><span class="mark"></span><span><em>Welcome to</em> Kestrel Bond House</span></h2>
  <p>Duis autem vel eum iriure dolor in hendrerit in vulputate velit esse molestieconsequat, vel illum dolore eu feugiat nulla facilisis at vero eros et accumsan et iusto odio dignissim qui blandit praesent luptatum zzril delenit augue duis dolore te feugait nulla facilisi.</p>
  <h4>Lorem ipsum dolor sit amet, consectetuer adipiscing elit,</h4>
  <p>sed diam nonummy ni euismod tincidunt ut laoreet dolore magna aliquam er volutpat. Ut wisi enim ad minim veniam, quis nostrud exerci tation ullamcorper suscipit lobortis ni ut aliquip ex consequat. Duis autem vel eum iriure dolor in hendrerit in vulputate velit esse molest consequat, vel illum dolore eu feugiat nulla facilisis at vero eros.</p>
  <a class="read">READ MORE</a>
</section>
<div class="welcome-rule"></div>

<section class="perks">
  <div class="perk">
    <div class="box"></div>
    <div class="icon"><svg width="24" height="22" viewBox="0 0 24 22"><path d="M2 8 12 2l10 6z" fill="#fff"/><rect x="4" y="9" width="16" height="10" fill="none" stroke="#fff" stroke-width="2"/><circle cx="12" cy="14" r="2.5" fill="none" stroke="#fff" stroke-width="1.5"/><rect x="1" y="19" width="22" height="2" fill="#fff"/></svg></div>
    <h5>100% Free of Charge</h5>
    <p>No hidden costs or service charges. Our fee is not hidden within the finance...</p>
    <a class="more">More »</a>
  </div>
  <div class="perk">
    <div class="box"></div>
    <div class="icon"><svg width="26" height="26" viewBox="0 0 26 26"><circle cx="13" cy="13" r="10" fill="none" stroke="#fff" stroke-width="3" stroke-dasharray="3 2"/><circle cx="13" cy="13" r="7" fill="#fff"/><path d="M9.5 13l2.5 2.5 4.5-5" fill="none" stroke="var(--blue)" stroke-width="2"/></svg></div>
    <h5>Exceptional Service</h5>
    <p>We guaruntee a first class service to you. Our home loan specialists...</p>
    <a class="more">More »</a>
  </div>
  <div class="perk">
    <div class="box"></div>
    <div class="icon"><svg width="26" height="24" viewBox="0 0 26 24"><rect x="2" y="8" width="18" height="13" rx="2" fill="none" stroke="#fff" stroke-width="2"/><path d="M10 15 22 3l2 2-12 12-3 1z" fill="#fff"/></svg></div>
    <h5>Credit Help</h5>
    <p>Problems with your credit record? We will do our best to help you...</p>
    <a class="more">More »</a>
  </div>
</section>

<section class="lenders">
  <h2><em>We Raise</em> Your Home Loan With</h2>
  <div class="lender-row">
    <span class="lender lender-a"><i></i>Karoo Trust</span>
    <span class="lender lender-b"><i></i>Marula Bank</span>
    <span class="lender lender-c"><i></i>Vantis</span>
    <span class="lender lender-d"><i></i>Highveld Bank</span>
  </div>
  <span class="pager" style="left:81px"><svg width="8" height="9" viewBox="0 0 8 9"><path d="M6 1 2 4.5 6 8" fill="none" stroke="#333" stroke-width="2"/></svg></span>
  <span class="pager" style="left:735px"><svg width="8" height="9" viewBox="0 0 8 9"><path d="M2 1l4 3.5L2 8" fill="none" stroke="#333" stroke-width="2"/></svg></span>
</section>

<footer class="site-footer">
  <div class="fcol f-links">
    <h3>Quick Links</h3>
    <ul><li>Home</li><li>About Us</li><li>Information</li><li>Calculators</li><li>Apply Online</li><li>Contact Us</li></ul>
  </div>
  <div class="f-rule" style="left:196px"></div>
  <div class="fcol f-news">
    <h3>Newsletter Signup</h3>
    <p>Lorem ipsum dolor sit amet,consecte adipiscing elit, sed diam nonummy ni euismod tincidunt.</p>
    <div class="field">Email Address</div>
    <span class="sub">SUBSCRIBE</span>
  </div>
  <div class="f-rule" style="left:401px"></div>
  <div class="fcol f-contact">
    <h3>Contact Detail</h3>
    <div class="c-row" style="top:35px"><svg width="10" height="13" viewBox="0 0 10 13"><path d="M5 0a5 5 0 0 1 5 5c0 3-5 8-5 8S0 8 0 5a5 5 0 0 1 5-5z" fill="#fff"/><circle cx="5" cy="5" r="1.8" fill="var(--footer)"/></svg><span>Unit 8 Brennan Court,<br>Lindell Close,<br>Midridge, 1682</span></div>
    <div class="c-row" style="top:86px"><svg width="10" height="11" viewBox="0 0 10 11"><path d="M2 0l2 3-1 1.5c.7 1.5 1.8 2.6 3 3.3L7.5 7 10 9l-1.5 2C4 10.5 0 6 0 1.5z" fill="#fff"/></svg><span>(010) 555 0142</span></div>
    <div class="c-row" style="top:109px"><svg width="11" height="10" viewBox="0 0 11 10"><rect x="2.5" y="0" width="6" height="3" fill="#fff"/><rect x="0" y="3.5" width="11" height="4.5" rx="1" fill="#fff"/><rect x="2.5" y="6" width="6" height="4" fill="#fff" stroke="var(--footer)"/></svg><span>(011) 555 0187</span></div>
    <div class="c-row" style="top:131px"><svg width="11" height="8" viewBox="0 0 11 8"><rect width="11" height="8" fill="#fff"/><path d="M0 0l5.5 4.5L11 0" fill="none" stroke="var(--footer)" stroke-width="1.2"/></svg><span>info@kestrelbondhouse.co.za</span></div>
    <div class="map" role="img" aria-label="Street map showing the office location in Johannesburg"></div>
  </div>
</footer>

<div class="bottom-bar">
  <span class="copy">Copyright © 2014 Kestrel Bond House (Pty) Ltd.</span>
  <span class="follow">Follow Us: <i></i><i></i><i></i><i></i></span>
</div>

</body>
</html>
```